Real estate company needs a letterhead design

A young real estate company needs a letterhead / stationery design, it should include the company's logo. It should look exactly the same as on the business cards. (With the phrase "a brand of KEV Wohnbau & Grundstücksentwicklung GmbH")

In addition, it should also include the 4 round seals.

color code blue # 00456b gray # 333333

Word and PDF are welcome.

KEV Wohnbau & Grundstücksentwicklung GmbH
Managing director: Mag. Lukas Fellnhuber
Matthias-Ortner-Strasse 3c / 41
6300 Wörgl

Tel .: +436648172093
Email: office@wohnglanz-beispiel.at
Web: www.wohnglanz-beispiel.at

Sparkasse Almtal, Bergländer Sparkasse from 1882, Genossenschaftskasse
Anton-Weissauer-Strasse 7, 6300 Wörgl
IBAN: AT31 4817 2964 0058 2316
BIC: GLMTAT44XXX
Account holder: KEV Wohnbau & Grundstücksentwicklung GmbH

FN: XXXXXXX
UID: XXXXXXX

```html
<!DOCTYPE html>
<html lang="en">
<head>
<meta charset="utf-8">
<title>WOHNGLANZ Letterhead</title>
<link href="https://fonts.googleapis.com/css2?family=Lato:wght@400;700;900&family=Open+Sans:wght@400;600&display=swap" rel="stylesheet">
<style>
  :root{
    --brand-blue:#00456b;
    --brand-gray:#333333;
    --text-body:#5a5a5a;
    --backdrop:#e6e6e6;
    --paper:#ffffff;
    --seal-red:#e2231a;
  }
  *{margin:0;padding:0;box-sizing:border-box}
  html,body{width:1040px;height:1200px;overflow:hidden;background:var(--backdrop)}
  .page{position:absolute;left:54px;top:0;width:932px;height:1200px;background:var(--paper);overflow:hidden;font-family:"Open Sans",Arial,sans-serif;color:var(--text-body)}
  .abs{position:absolute}

  .brand-name{left:88px;top:84px;font-family:"Lato",Arial,sans-serif;font-weight:900;font-size:48px;letter-spacing:1px;color:var(--brand-blue);line-height:1}
  .brand-name sup{font-size:18px;font-weight:400;vertical-align:top;margin-left:4px}
  .brand-tagline{left:89px;top:145px;width:445px;height:31px;background:var(--brand-blue);color:#fff;font-family:"Lato",Arial,sans-serif;font-size:13px;line-height:31px;padding-left:10px;text-transform:uppercase;white-space:nowrap}

  .header-divider{left:566px;top:30px;width:1px;height:150px;background:#cfcfcf}
  .contact{left:582px;top:30px;font-family:"Lato",Arial,sans-serif;color:var(--brand-gray);font-size:15px;line-height:20px}
  .contact-name{font-weight:700;font-size:18px;color:var(--brand-blue);text-transform:uppercase}
  .contact-list{list-style:none;margin-top:10px}
  .contact-list li{display:flex;align-items:center;gap:7px}
  .contact-list svg{width:13px;height:13px;flex:none}
  .contact-address{margin-top:10px;padding-left:3px}

  .letter{left:98px;top:218px;width:753px;font-size:14.5px}
  .issue-date{margin-bottom:22px}
  .recipient{line-height:18px;margin-bottom:50px}
  .salutation{margin-bottom:32px}
  .letter p.body{line-height:27px;text-align:justify;margin-bottom:26px}
  .closing{margin-top:50px;line-height:28px}
  .signer{font-size:18px;font-weight:600;color:var(--brand-gray)}

  .seals{left:96px;top:989px;display:flex;gap:6px}
  .seal{width:84px;height:84px;border-radius:50%;border:2px solid var(--seal-red);display:flex;align-items:center;justify-content:center}
  .seal span{width:46px;height:46px;border-radius:50%;background:var(--seal-red);display:block}

  .footer-art{left:0;top:1083px}
  .bank-details{left:107px;top:1094px;font-family:"Lato",Arial,sans-serif;color:#fff;font-size:15px;line-height:20px}
  .bank-details .gap{margin-top:4px}
  .registry{left:658px;top:1120px;font-family:"Lato",Arial,sans-serif;color:#fff;font-size:15px;line-height:20px}
</style>
</head>
<body>
<main class="page">
  <header>
    <div class="abs brand-name">WOHNGLANZ<sup>®</sup></div>
    <div class="abs brand-tagline">A brand of KEV Wohnbau &amp; Grundstücksentwicklung GmbH</div>
    <div class="abs header-divider"></div>
    <div class="abs contact">
      <div class="contact-name">Mag. Lukas Fellnhuber</div>
      <div>Managing Director</div>
      <ul class="contact-list">
        <li><svg viewBox="0 0 14 14"><rect width="14" height="14" rx="3" fill="#00456b"/><path d="M4.2 3.3l1.6 1.6-.9 1.1c.6 1.2 1.5 2.1 2.7 2.7l1.1-.9 1.6 1.6-1 1.3C6.6 10.5 3.5 7.4 3 4.3z" fill="#fff"/></svg>+436648172093</li>
        <li><svg viewBox="0 0 14 14"><rect width="14" height="14" rx="3" fill="#00456b"/><rect x="3" y="4.2" width="8" height="5.6" fill="none" stroke="#fff" stroke-width="1.1"/><path d="M3 4.4l4 3 4-3" fill="none" stroke="#fff" stroke-width="1.1"/></svg>office@wohnglanz-beispiel.at</li>
        <li><svg viewBox="0 0 14 14"><rect width="14" height="14" rx="3" fill="#00456b"/><circle cx="7" cy="7" r="4" fill="none" stroke="#fff" stroke-width="1"/><path d="M3 7h8M7 3c-2 2.4-2 5.6 0 8M7 3c2 2.4 2 5.6 0 8" fill="none" stroke="#fff" stroke-width=".9"/></svg>www.wohnglanz-beispiel.at</li>
      </ul>
      <div class="contact-address">Matthias-Ortner-Strasse 3c / 41<br>6300 Wörgl</div>
    </div>
  </header>

  <section class="abs letter">
    <div class="issue-date">Issuing Date: May 5, 2018</div>
    <div class="recipient">Name Of Employee Mr. XYZABC<br>Address of Employee<br>Address Line 2 etc..</div>
    <div class="salutation">Dear Mr.XYZABC</div>
    <p class="body">Lorem Ipsum has been the industry's standard dummy text ever since the 1500s, when an unknown printer took a galley of type and scrambled it to make a type specimen book. It has survived not only five centuries, but also the leap into electronic typesetting, remaining essentially unchanged. It was popularised in the 1960s with the release of Lettrafix sheets containing Lorem Ipsum passages, and more recently with desktop publishing software like Pagewright Studio including versions of Lorem Ipsum.</p>
    <p class="body">Lorem Ipsum is simply dummy text of the printing and typesetting industry. Lorem Ipsum has been the industry's standard dummy text ever since the 1500s, when an unknown printer took a galley of type and scrambled it to make a type specimen book.</p>
    <p class="body">It has survived not only five centuries, but also the leap into electronic typesetting, remaining essentially unchanged. It was popularised in the 1960s with the release of Lettrafix sheets containing Lorem IpsumIpsum passages.</p>
    <div class="closing">
      <div>Yours Sincerely</div>
      <div class="signer">Jonas Berger</div>
      <div>Managing Director</div>
    </div>
  </section>

  <div class="abs seals">
    <div class="seal" role="img" aria-label="Certification seal"><span></span></div>
    <div class="seal" role="img" aria-label="Certification seal"><span></span></div>
    <div class="seal" role="img" aria-label="Certification seal"><span></span></div>
    <div class="seal" role="img" aria-label="Certification seal"><span></span></div>
  </div>

  <footer>
    <svg class="abs footer-art" width="932" height="117" viewBox="0 0 932 117">
      <rect x="0" y="0" width="771" height="117" fill="#333333"/>
      <polygon points="771,0 798,22 771,22" fill="#1f2a33"/>
      <rect x="639" y="22" width="159" height="72" fill="#00456b"/>
      <polygon points="771,94 798,94 771,117" fill="#0b2c42"/>
    </svg>
    <div class="abs bank-details">
      <div>IBAN: AT31 4817 2964 0058 2316 | BIC: GLMTAT44XXX</div>
      <div>Account holder: KEV Wohnbau &amp; Grundstücksentwicklung GmbH</div>
      <div class="gap">Sparkasse Almtal, Bergländer Sparkasse from 1882, Genossenschaftskasse</div>
      <div>Anton-Weissauer-Strasse 7, 6300 Wörgl</div>
    </div>
    <div class="abs registry">FN: XXXXXXX<br>UID: XXXXXXX</div>
  </footer>
</main>
</body>
</html>
```